Business card design for Virtual Assistance company

I need a business card designed for my virtual assistance company. We are a small company who services primarily C-level executive clients. The card needs to be double sided with the following contact information on the back:
Melanie Hartwick
Owner/CEO
info@pbtadvisory.net
www.pbtadvisory.net
240.395.2817

The front side should just have the company name incorporated: "PBT Advisory" and "virtual assistance"

The card should be simplistic, but eye catching and should speak to high level executives. Our primary focus areas consist of executive assistance and government contracting.

Target Market(s)

CEOs and executives

Contact Information for Business Card

see project description. phone, email, website.

Colors

Designer to choose only greyscale colors for use in the design.

```html
<!DOCTYPE html>
<html lang="en">
<head>
<meta charset="utf-8">
<title>PBT Advisory — Business Card</title>
<link href="https://fonts.googleapis.com/css2?family=Crimson+Pro:wght@400;600&display=swap" rel="stylesheet">
<style>
  :root {
    --backdrop: #dcdcdc;
    --paper: #f1f1f1;
    --ink: #2a2a2a;
    --ink-soft: #3a3a3a;
    --shadow: rgba(0, 0, 0, 0.18);
  }
  * { box-sizing: border-box; margin: 0; padding: 0; }
  html, body {
    width: 1200px;
    height: 900px;
    overflow: hidden;
    background: var(--backdrop);
    font-family: "Crimson Pro", Georgia, serif;
    color: var(--ink);
  }
  .sheet {
    width: 1200px;
    height: 900px;
    display: flex;
    flex-direction: column;
    align-items: center;
    justify-content: center;
    gap: 44px;
  }
  .card {
    position: relative;
    width: 620px;
    height: 354px;
    background: var(--paper);
    box-shadow: 0 10px 28px var(--shadow);
    overflow: hidden;
  }

  /* Front side */
  .card--front {
    display: flex;
    flex-direction: column;
    align-items: center;
    justify-content: center;
    gap: 14px;
  }
  .brand-name {
    font-weight: 600;
    font-size: 40px;
    letter-spacing: 0.06em;
    text-transform: uppercase;
    color: var(--ink);
  }
  .tagline {
    display: flex;
    align-items: center;
    gap: 12px;
    font-weight: 600;
    font-size: 14px;
    letter-spacing: 0.5em;
    text-transform: uppercase;
    color: var(--ink-soft);
  }
  .tagline::before,
  .tagline::after {
    content: "";
    width: 26px;
    height: 1px;
    background: var(--ink-soft);
  }

  /* Back side */
  .decor-block {
    position: absolute;
    left: 0;
    bottom: 0;
    width: 200px;
    height: 250px;
    background: var(--ink);
  }
  .contact {
    position: absolute;
    right: 34px;
    top: 112px;
    text-align: right;
  }
  .contact__name {
    font-weight: 600;
    font-size: 27px;
    letter-spacing: 0.04em;
    text-transform: uppercase;
    line-height: 1;
  }
  .contact__role {
    font-size: 19px;
    margin-top: 6px;
  }
  .contact__list {
    list-style: none;
    margin-top: 34px;
    display: flex;
    flex-direction: column;
    gap: 8px;
  }
  .contact__item {
    display: flex;
    justify-content: flex-end;
    align-items: center;
    gap: 12px;
    font-size: 17px;
    letter-spacing: 0.08em;
  }
  .contact__icon {
    width: 14px;
    height: 14px;
    flex: none;
  }
</style>
</head>
<body>
<main class="sheet">
  <section class="card card--front" aria-label="Card front">
    <h1 class="brand-name">PBT Advisory</h1>
    <p class="tagline">Virtual Assistance</p>
  </section>

  <section class="card card--back" aria-label="Card back">
    <div class="decor-block"></div>
    <div class="contact">
      <h2 class="contact__name">Melanie Hartwick</h2>
      <p class="contact__role">Owner/CEO</p>
      <ul class="contact__list">
        <li class="contact__item">240.395.2817
          <svg class="contact__icon" viewBox="0 0 16 16" aria-hidden="true">
            <path d="M4 1.5l2 3-1.3 1.4c.8 1.9 2.4 3.5 4.4 4.4L10.5 9l3 2-.8 2.6c-.3.6-1 .9-1.7.7C6.5 13 3 9.5 1.7 5c-.2-.7.1-1.4.7-1.7z" fill="none" stroke="#2a2a2a" stroke-width="1.3" stroke-linejoin="round"/>
          </svg>
        </li>
        <li class="contact__item">info@pbtadvisory.net
          <svg class="contact__icon" viewBox="0 0 16 16" aria-hidden="true">
            <rect x="1" y="3.5" width="14" height="9" fill="#2a2a2a"/>
            <path d="M1.5 4l6.5 5 6.5-5" fill="none" stroke="#f1f1f1" stroke-width="1"/>
          </svg>
        </li>
        <li class="contact__item">pbtadvisory.net
          <svg class="contact__icon" viewBox="0 0 16 16" aria-hidden="true">
            <circle cx="8" cy="8" r="6.8" fill="#2a2a2a"/>
            <path d="M8 1.2v13.6M1.2 8h13.6M8 1.2c-3 3.4-3 10.2 0 13.6M8 1.2c3 3.4 3 10.2 0 13.6" fill="none" stroke="#f1f1f1" stroke-width="0.8"/>
          </svg>
        </li>
      </ul>
    </div>
  </section>
</main>
</body>
</html>
```